Web Design for online C2C site

We need a web design for a brand new website that has users logging into an account and uploading pictures of goods and services that they want to trade.
We like 'fresh' and simple websites that have a white background, with easy navigation, a splash of colour (grey, blue, and green is a colour scheme that appeals to us) but doesn't look overly boring.
The site needs a modern look for an old type of trade - a barter system.
We have attached a file with our logo and would like to use the top logo from the file (grey, green, and blue)
Updates
Project Deadline Extended
Reason: The timeline has been extended until this Sunday, December 2nd for all who require extra time to design a web layout.
Cheers,
Margot
Industry/Entity Type
Trade
Look and feel
Each slider illustrates characteristics of the customer's brand and the style your logo design should communicate.

```html
<!DOCTYPE html>
<html lang="en">
<head>
<meta charset="utf-8">
<title>BarterLoop – Home</title>
<link href="https://fonts.googleapis.com/css2?family=Ubuntu:ital,wght@0,400;0,500;0,700;1,400&display=swap" rel="stylesheet">
<style>
:root{
  --blue:#0a95e8;
  --blue-deep:#1b6fd0;
  --blue-text:#1a5ea8;
  --green:#5cbf1c;
  --grey-dark:#3a3634;
  --grey-bar:#2e2e2e;
  --grey-mid:#8f8f8f;
  --grey-light:#dcdcdc;
  --field:#e7e7e7;
  --ink:#333;
  --white:#fff;
  --header-top:#f9f9f9;
  --header-bottom:#ececec;
}
*{margin:0;padding:0;box-sizing:border-box}
html,body{width:1152px;height:1200px;overflow:hidden;background:var(--white);font-family:"Ubuntu",sans-serif;color:var(--ink)}
.page{position:relative;width:1152px;height:1200px}

/* header */
.site-header{position:absolute;left:0;top:0;width:1152px;height:175px;background:linear-gradient(var(--header-top),var(--header-bottom))}
.header-strip{position:absolute;left:0;top:0;width:1152px;height:14px;background:var(--grey-dark)}
.brand{position:absolute;left:36px;top:44px;display:flex;align-items:center;gap:14px}
.brand-mark{width:82px;height:82px;border-radius:50%;background:var(--grey-mid)}
.brand-name{font-size:38px;font-weight:700;color:var(--blue-deep)}

.social-tab{position:absolute;left:414px;top:0;width:224px;height:52px;background:var(--grey-dark);border-radius:0 0 22px 22px;display:flex;gap:10px;justify-content:center;align-items:center}
.social-dot{width:34px;height:34px;border-radius:50%;background:#54504d;border:2px solid #2a2725}
.tooltip{position:absolute;left:511px;top:54px;width:123px;height:20px;background:#555;color:#eee;font-size:12px;line-height:20px;text-align:center}

.login-tab{position:absolute;left:684px;top:0;width:440px;height:52px;background:var(--grey-dark);border-radius:0 0 22px 22px}
.login-label{position:absolute;left:12px;top:14px;color:#9fd3f7;font-size:19px}
.login-field{position:absolute;top:9px;height:32px;border-radius:16px;background:#5a5654;color:#bbb;font-style:italic;font-size:19px;line-height:32px;padding-left:16px}
.login-go{position:absolute;left:396px;top:9px;width:32px;height:32px}

/* nav */
.main-nav{position:absolute;left:0;top:175px;width:1152px;height:75px;background:var(--blue);border-top:14px solid var(--blue-deep);box-shadow:0 6px 8px -6px #bbb}
.nav-item{position:absolute;top:16px;color:var(--white);font-size:23px}
.nav-item.active{left:44px;top:-13px;width:148px;height:62px;background:var(--white);color:var(--blue-text);border-radius:3px;text-align:center;line-height:62px}
.search{position:absolute;left:898px;top:9px;width:238px;height:36px;background:var(--white);border-radius:18px;border:1px solid #bcd}
.search span{position:absolute;left:16px;top:8px;font-style:italic;color:#4a90c8;font-size:17px}
.search svg{position:absolute;right:1px;top:1px}

/* slider */
.slider{position:absolute;left:68px;top:307px;width:1018px;height:390px;background:#f7f7f7;box-shadow:0 10px 10px -8px #ccc}
.slider-arrow{position:absolute;top:0;width:42px;height:390px;background:linear-gradient(90deg,#2c2c2c,#454545,#2c2c2c)}
.slider-arrow.prev{left:0}.slider-arrow.next{right:0}
.slider-arrow svg{position:absolute;left:11px;top:180px}
.slide-brand{position:absolute;left:170px;top:115px;display:flex;align-items:center;gap:22px}
.slide-mark{width:150px;height:150px;border-radius:50%;background:var(--grey-mid)}
.slide-name{font-size:74px;font-weight:700;color:var(--blue-deep)}
.slider-dots{position:absolute;left:444px;top:362px;display:flex;gap:20px;align-items:center}
.dot{width:16px;height:16px;border-radius:50%;background:#eee;border:1px solid #aaa}
.dot.current{width:22px;height:22px;background:#5da8f0;border-color:#3c87d6}

/* listings */
.listings{position:absolute;left:37px;top:787px;width:631px;height:383px;background:#f9f9f9;border:1px solid #e4e4e4}
.list-tabs{display:flex;height:42px}
.list-tab{height:42px;background:var(--grey-light);border-bottom:6px solid #a8a8a8;font-size:21px;line-height:38px;padding-left:20px}
.list-tab.active{background:var(--white);border-bottom:none;color:#222;padding-left:30px}
.list-divider{position:absolute;left:276px;top:77px;width:1px;height:306px;background:#aaa}
.item-photo{position:absolute;border-radius:6px}
.item-photo.laptop{left:35px;top:100px;width:108px;height:78px;background:linear-gradient(135deg,#4aa0a8,#9dc 55%,#b8b8b8)}
.item-photo.phone{left:318px;top:143px;width:70px;height:130px;background:linear-gradient(#222,#3b4a7a 40%,#222);border-radius:10px}
.item-text{position:absolute;font-size:17px;line-height:21.6px;color:#333}
.item-text.left{left:15px;top:190px;width:170px;text-align:center}
.item-text.right{left:418px;top:130px;width:170px}
.play{position:absolute;top:346px}

/* join panel */
.join{position:absolute;left:742px;top:742px;width:364px;height:424px;background:var(--white);border-radius:6px;box-shadow:0 1px 5px #bbb;overflow:hidden}
.join-tabs{display:flex;height:45px}
.join-tab{width:171px;font-size:21px;line-height:45px;text-align:center;color:var(--blue-text);font-weight:500;background:var(--white)}
.join-tab.alt{width:193px;background:var(--blue);color:var(--white);font-weight:400;border-radius:6px 6px 0 0}
.join-band{height:18px;background:var(--blue);border-radius:6px 0 0 0}
.field{position:absolute;left:62px;width:266px;height:38px;border-radius:19px;background:var(--field);border:1px solid #ccc;box-shadow:inset 0 2px 3px #ccc;color:#666;font-size:18px;line-height:36px;padding-left:22px}
.signup{position:absolute;left:212px;top:316px;width:114px;height:38px;border-radius:8px;background:linear-gradient(#666,#3a3a3a);color:var(--white);font-size:19px;line-height:38px;text-align:center;box-shadow:0 1px 3px #777}
.forgot{position:absolute;left:28px;top:374px;font-size:15px;color:#333}
.join-foot{position:absolute;left:0;bottom:0;width:364px;height:22px;background:var(--blue)}
</style>
</head>
<body>
<div class="page">
  <header class="site-header">
    <div class="header-strip"></div>
    <div class="brand"><div class="brand-mark"></div><span class="brand-name">BarterLoop</span></div>
    <div class="social-tab">
      <span class="social-dot"></span><span class="social-dot"></span><span class="social-dot"></span><span class="social-dot"></span><span class="social-dot"></span>
    </div>
    <div class="tooltip">Follow us</div>
    <div class="login-tab">
      <span class="login-label">Log in</span>
      <span class="login-field" style="left:72px;width:152px">Email</span>
      <span class="login-field" style="left:235px;width:153px">Password</span>
      <svg class="login-go" viewBox="0 0 32 32"><circle cx="16" cy="16" r="13" fill="none" stroke="#fff" stroke-width="3"/><path d="M9 16h13M17 10l6 6-6 6" fill="none" stroke="#fff" stroke-width="3"/></svg>
    </div>
  </header>

  <nav class="main-nav">
    <span class="nav-item active">Home</span>
    <span class="nav-item" style="left:230px">Page</span>
    <span class="nav-item" style="left:333px">About us</span>
    <span class="nav-item" style="left:467px">Contact us</span>
    <div class="search"><span>Search.....</span>
      <svg width="34" height="34" viewBox="0 0 34 34"><circle cx="17" cy="17" r="16" fill="#2a4f6e"/><circle cx="16" cy="15" r="7" fill="none" stroke="#fff" stroke-width="2"/><path d="M21 20l5 5" stroke="#fff" stroke-width="2.5"/></svg>
    </div>
  </nav>

  <section class="slider">
    <div class="slider-arrow prev"><svg width="20" height="30" viewBox="0 0 20 30"><path d="M16 3L4 15l12 12" fill="none" stroke="#eee" stroke-width="3"/></svg></div>
    <div class="slide-brand"><div class="slide-mark"></div><span class="slide-name">BarterLoop</span></div>
    <div class="slider-arrow next"><svg width="20" height="30" viewBox="0 0 20 30"><path d="M4 3l12 12L4 27" fill="none" stroke="#eee" stroke-width="3"/></svg></div>
    <div class="slider-dots"><span class="dot"></span><span class="dot current"></span><span class="dot"></span><span class="dot"></span></div>
  </section>

  <section class="listings">
    <div class="list-tabs">
      <div class="list-tab" style="width:175px">Most Recent</div>
      <div class="list-tab active" style="width:212px">Most Popular</div>
      <div class="list-tab" style="width:244px">Deal of the day</div>
    </div>
    <div class="item-photo laptop" role="img" aria-label="Laptop offered for swap"></div>
    <p class="item-text left">this is just as example. this is just as example. this is just as example. this is just as example. this is just as example. this is just</p>
    <svg class="play" style="left:204px" width="30" height="30" viewBox="0 0 30 30"><circle cx="15" cy="15" r="15" fill="#000"/><path d="M12 9l9 6-9 6z" fill="#fff"/></svg>
    <div class="list-divider"></div>
    <div class="item-photo phone" role="img" aria-label="Smartphone offered for swap"></div>
    <p class="item-text right">&nbsp;&nbsp;this is just as example. this is just as example. this is just as example. this is just as example. this is just as example. this is just</p>
    <svg class="play" style="left:561px" width="30" height="30" viewBox="0 0 30 30"><circle cx="15" cy="15" r="15" fill="#000"/><path d="M12 9l9 6-9 6z" fill="#fff"/></svg>
  </section>

  <aside class="join">
    <div class="join-tabs"><div class="join-tab">Join Now</div><div class="join-tab alt">Sign in</div></div>
    <div class="join-band"></div>
    <div class="field" style="top:108px">Username</div>
    <div class="field" style="top:156px">Email</div>
    <div class="field" style="top:206px">Password</div>
    <div class="field" style="top:254px">Confirm password</div>
    <div class="signup">Sign up</div>
    <span class="forgot">Forgot your email?</span>
    <div class="join-foot"></div>
  </aside>
</div>
</body>
</html>
```